Page for a flyer

I need a page designed that is 8.5" wide and 5.5" height. I need the left half of the page to be vintage looking in color and texture and the other half to be plain white and look like it is ripped down the middle

```html
<!DOCTYPE html>
<html lang="en">
<head>
<meta charset="utf-8">
<title>Flyer Page – Torn Kraft Paper</title>
<style>
  :root {
    --page-white: #ffffff;
    --kraft-light: #d2a877;
    --kraft-mid: #c39762;
    --kraft-dark: #ad8250;
    --tear-edge: #ffffff;
    --tear-shadow: #2e2e2e;
  }
  html, body {
    margin: 0;
    padding: 0;
    width: 1200px;
    height: 789px;
    overflow: hidden;
    background: var(--page-white);
  }
  .flyer-page {
    position: relative;
    width: 1200px;
    height: 789px;
    background: var(--page-white);
  }
  .flyer-page svg {
    display: block;
    width: 1200px;
    height: 789px;
  }
  .tear-shadow { fill: var(--tear-shadow); opacity: 0.6; }
  .tear-edge { fill: var(--tear-edge); }
</style>
</head>
<body>
<main class="flyer-page">
  <svg viewBox="0 0 1200 789" xmlns="http://www.w3.org/2000/svg">
    <defs>
      <radialGradient id="kraftTone" cx="40%" cy="45%" r="80%">
        <stop offset="0%" stop-color="var(--kraft-light)"/>
        <stop offset="65%" stop-color="var(--kraft-mid)"/>
        <stop offset="100%" stop-color="var(--kraft-dark)"/>
      </radialGradient>

      <filter id="crumpledPaper" x="0" y="0" width="100%" height="100%" color-interpolation-filters="sRGB">
        <feTurbulence type="fractalNoise" baseFrequency="0.006 0.009" numOctaves="6" seed="7" result="folds"/>
        <feDiffuseLighting in="folds" surfaceScale="4" diffuseConstant="1" lighting-color="#ffffff" result="foldLight">
          <feDistantLight azimuth="225" elevation="58"/>
        </feDiffuseLighting>
        <feTurbulence type="fractalNoise" baseFrequency="0.9" numOctaves="2" seed="3" result="grain"/>
        <feColorMatrix in="grain" type="matrix"
          values="0 0 0 0 0.5  0 0 0 0 0.5  0 0 0 0 0.5  0 0 0 0.18 0" result="grainSoft"/>
        <feComposite in="SourceGraphic" in2="foldLight" operator="arithmetic" k1="1.22" k2="0" k3="0" k4="0" result="creased"/>
        <feBlend in="grainSoft" in2="creased" mode="multiply" result="grained"/>
        <feComposite in="grained" in2="SourceGraphic" operator="in"/>
      </filter>

      <filter id="softShadow" x="-10%" y="-10%" width="120%" height="120%">
        <feGaussianBlur stdDeviation="4"/>
      </filter>

      <path id="tornSheet" d="M0 0 L614 0 L611 12 L618 22 L612 30 L622 34 L608 46 L600 52 L606 60 L602 72 L610 84 L604 98 L612 112 L606 130 L610 142 L598 156 L590 168 L582 176 L586 190 L580 200 L590 206 L576 212 L594 218 L604 226 L600 240 L606 258 L598 270 L608 282 L590 286 L604 294 L614 300 L598 306 L586 314 L606 318 L596 328 L616 328 L606 342 L596 352 L590 362 L594 380 L588 398 L580 408 L562 416 L556 428 L546 436 L560 440 L566 448 L562 464 L568 480 L566 500 L558 514 L566 528 L562 548 L570 566 L560 580 L552 590 L542 600 L536 612 L546 620 L544 634 L552 650 L550 664 L560 672 L558 688 L566 698 L570 712 L566 724 L576 736 L584 752 L592 766 L600 778 L602 789 L0 789 Z"/>
    </defs>

    <use href="#tornSheet" class="tear-shadow" transform="translate(20 7)" filter="url(#softShadow)"/>
    <use href="#tornSheet" class="tear-edge" transform="translate(12 0)"/>
    <g class="kraft-panel" role="img" aria-label="Vintage crumpled brown kraft paper texture">
      <use href="#tornSheet" fill="url(#kraftTone)" filter="url(#crumpledPaper)"/>
    </g>
  </svg>
</main>
</body>
</html>
```